Real Estate Flyer (Brenton Property)

We need a color CMYK high resolution, print quality horizontal real estate property flyer designed in the sizes of 10" wide and 6.7425" tall and another one in 11" wide and 8.5" tall.
Ad should be professionally looking to U.S. standards. It should be sleek, modern yet classy.
We uploaded in Briefs logo files, agent photo, 2 photos of the property (Must use both) and a sample of a flyer for Vayle Morrow Luxury Residence. We like how the overlay atop the first photo in the Vayle Morrow flyer with the company logo in the overlay. We'd like to incorporate that with our logo, the background color of the overlay should match that of our logo. DON'T CHANGE LOGO COLORS. Only use two colors in ad (exact logo blue color and white). The text in the overlay must be "FOR SALE - Potential Income Producing Commercial Office Building". Other details that should be prominent underneath are "42 Brenton Dr., Schaumburg, IL 60174 - Asking Price: $650,000".
Add "Residential & Commercial" under our company logo in italic font.
Add in flyer: "Located seconds away from the Kettering Rd. & Palden Rd. Intersection"
Add in flyer:
- Completely vacant
- 10,000 sq. ft. building
- 55 Car Parking
- 1.38 acre lot
- Over 20 offices and 5 bathrooms.
- Lease out individual office spaces for great monthly cash flow
Put agent's photo and following details professionally displayed:
Dev Marlo
Managing Broker
847-555-0148
dev.marlo@qtnhomes-example.com
Add from Briefs fair housing logo and PLX logo near agent's information. Logos should be small but yet visible to understand text.
Add at bottom of the ad with separation near agent details:
Looking to Buy or Sell?
I’m your one-stop, full service licensed real estate broker.
I deal with all types of real estate properties: Homes, Condos, Townhomes, Multi-Unit Apartment Buildings and Commercial Spaces.
Let My Experience Guide You Through Every Step of the Process!
Fine print:
©2018 QTN Homes, Inc. All Rights Reserved.

```html
<!DOCTYPE html>
<html lang="en">
<head>
<meta charset="utf-8">
<title>Brenton Property – For Sale Flyer</title>
<link rel="stylesheet" href="https://fonts.googleapis.com/css2?family=Oswald:wght@400;500;600&family=Open+Sans:ital,wght@0,400;0,600;0,700;1,400;1,600&display=swap">
<style>
  :root {
    --brand-blue: #1d5aa8;
    --brand-blue-deep: #164a8d;
    --overlay-blue: rgba(29, 90, 168, 0.9);
    --white: #ffffff;
    --ink: #1f2a3a;
    --muted: #4a5566;
    --page: #ffffff;
    --photo-sky: #b9c6d6;
    --photo-roof: #5a4a44;
    --photo-wall: #d9cdb8;
  }
  * { box-sizing: border-box; margin: 0; padding: 0; }
  html, body { width: 831px; height: 1200px; overflow: hidden; background: var(--page); }
  body { position: relative; font-family: "Open Sans", Arial, sans-serif; color: var(--ink); }

  .flyer {
    position: absolute; left: 25px; top: 337px;
    width: 781px; height: 526px;
    background: var(--white);
    box-shadow: 0 2px 10px rgba(0,0,0,0.18);
    overflow: hidden;
  }

  .property-photo {
    position: absolute; left: 0; top: 0; width: 781px; height: 306px;
    background: linear-gradient(180deg, var(--photo-sky) 0%, #a9b3bf 35%, var(--photo-roof) 48%, var(--photo-wall) 70%, #8b8f88 100%);
  }

  .title-band {
    position: absolute; left: 0; top: 206px; width: 781px; height: 100px;
    background: var(--overlay-blue);
    color: var(--white);
    padding: 10px 20px 0 22px;
  }
  .title-band .for-sale {
    font-family: "Open Sans", Arial, sans-serif; font-style: italic; font-weight: 700;
    font-size: 30px; line-height: 32px; letter-spacing: 0.5px;
  }
  .title-band .headline {
    font-family: "Oswald", Arial, sans-serif; font-weight: 500;
    font-size: 21px; line-height: 26px; letter-spacing: 0.3px;
  }
  .title-band .address {
    font-family: "Oswald", Arial, sans-serif; font-weight: 400;
    font-size: 16px; line-height: 22px;
  }

  .brand-lockup {
    position: absolute; right: 22px; top: 14px;
    width: 120px; height: 70px;
    background: var(--white); color: var(--brand-blue);
    display: flex; flex-direction: column; align-items: center; justify-content: center;
  }
  .brand-lockup .brand-name {
    display: flex; align-items: center; gap: 5px;
    font-family: "Open Sans", Arial, sans-serif; font-weight: 700; font-size: 17px;
  }
  .brand-lockup .brand-mark { width: 10px; height: 10px; background: var(--brand-blue); }
  .brand-lockup .brand-tag { font-style: italic; font-size: 9px; margin-top: 3px; }

  .agent-photo {
    position: absolute; left: 22px; top: 320px; width: 82px; height: 100px;
    background: linear-gradient(180deg, #e7e9ec 0%, #9aa3ae 55%, #2c3440 100%);
  }
  .agent-card { position: absolute; left: 114px; top: 320px; width: 172px; }
  .agent-card .agent-name { font-family: "Open Sans", Arial, sans-serif; font-weight: 700; font-size: 15px; line-height: 20px; color: var(--brand-blue); }
  .agent-card .agent-line { font-size: 10px; line-height: 13px; color: var(--muted); white-space: nowrap; }
  .agent-card .agent-email { font-size: 9.5px; }

  .cta-box {
    position: absolute; left: 112px; top: 388px; width: 150px; height: 34px;
    background: var(--brand-blue); color: var(--white);
    font-family: "Oswald", Arial, sans-serif; font-weight: 500; font-size: 12.5px; line-height: 14px;
    padding: 3px 10px;
    text-transform: uppercase;
  }

  .feature-panel {
    position: absolute; left: 288px; top: 306px; width: 493px; height: 120px;
    background: var(--brand-blue); color: var(--white);
    padding: 12px 22px;
  }
  .feature-panel .feature-head {
    font-family: "Oswald", Arial, sans-serif; font-weight: 500; font-size: 15px; letter-spacing: 0.6px;
    text-transform: uppercase; margin-bottom: 4px;
  }
  .feature-list { list-style: none; font-size: 11px; line-height: 15px; font-style: italic; }
  .feature-list li::before { content: "•"; margin-right: 7px; font-style: normal; }
  .feature-panel .location-note { position: absolute; right: 22px; top: 14px; font-size: 9.5px; font-style: italic; width: 150px; text-align: right; line-height: 13px; }

  .pitch {
    position: absolute; left: 22px; top: 438px; width: 737px;
    font-size: 10.5px; line-height: 15px; color: var(--ink);
  }
  .pitch .pitch-strong { font-weight: 700; color: var(--brand-blue); font-size: 12px; }
  .pitch .pitch-close { font-style: italic; font-weight: 600; }

  .fine-print {
    position: absolute; right: 22px; bottom: 10px;
    display: flex; align-items: center; gap: 8px;
    font-size: 8px; color: var(--muted);
  }
  .fine-print .badge { width: 16px; height: 16px; background: var(--brand-blue); }
  .fine-print .badge.round { border-radius: 50%; }
</style>
</head>
<body>
  <article class="flyer">
    <div class="property-photo" role="img" aria-label="Photo of the two-storey commercial office building with dormer roof and parking in front"></div>

    <header class="title-band">
      <p class="for-sale">FOR SALE</p>
      <h1 class="headline">POTENTIAL INCOME PRODUCING COMMERCIAL OFFICE BUILDING</h1>
      <p class="address">42 Brenton Dr., Schaumburg, IL 60174 – Asking Price: $650,000</p>
      <div class="brand-lockup">
        <div class="brand-name"><span class="brand-mark"></span>QTN Homes</div>
        <div class="brand-tag">Residential &amp; Commercial</div>
      </div>
    </header>

    <div class="agent-photo" role="img" aria-label="Portrait of the managing broker"></div>
    <div class="agent-card">
      <p class="agent-name">Dev Marlo</p>
      <p class="agent-line">Managing Broker</p>
      <p class="agent-line">847-555-0148</p>
      <p class="agent-line agent-email">dev.marlo@qtnhomes-example.com</p>
    </div>
    <div class="cta-box">Looking to<br>Buy or Sell?</div>

    <section class="feature-panel">
      <h2 class="feature-head">Completely Vacant</h2>
      <ul class="feature-list">
        <li>10,000 sq. ft. building</li>
        <li>55 Car Parking</li>
        <li>1.38 acre lot</li>
        <li>Over 20 offices and 5 bathrooms</li>
        <li>Lease out individual office spaces for great monthly cash flow</li>
      </ul>
      <p class="location-note">Located seconds away from the Kettering Rd. &amp; Palden Rd. Intersection</p>
    </section>

    <section class="pitch">
      <p>I’m your one-stop, full service licensed real estate broker. I deal with all types of real estate properties:</p>
      <p class="pitch-strong">Homes, Condos, Townhomes, Multi-Unit Apartment Buildings and Commercial Spaces.</p>
      <p class="pitch-close">Let My Experience Guide You Through Every Step of the Process!</p>
    </section>

    <footer class="fine-print">
      <span>©2018 QTN Homes, Inc. All Rights Reserved.</span>
      <span class="badge" aria-label="Fair housing badge"></span>
      <span class="badge round" aria-label="PLX badge"></span>
    </footer>
  </article>
</body>
</html>
```